Hello, our company is 'RVL Suppliers Inc.' and 'Durafilm Linings'. We like to go by 'RVL' and 'Durafilm Linings'.
We are not very happy with our card and we would like a redesign.

our RVL logo colours was red, black, and white, so that was our original theme. the Durafilm logo is blue and white, and we'd like to incoroprate that.
Also, we focus on municipal water market/systems so water is a theme. we use robots for pipe rehabilitation. We also work in industrial markets such as mines.

Please see the example of our front and back from our previous logo. I have attached our logos for you to determine which would be best to use.

We also carry a line called Velsun. Their logo could also be added in a smaller way.

```html
<!DOCTYPE html>
<html lang="en">
<head>
<meta charset="utf-8">
<title>RVL Suppliers Inc. – Business Card</title>
<link rel="stylesheet" href="https://fonts.googleapis.com/css2?family=Montserrat:wght@700;800&family=Lato:wght@400;700&display=swap">
<style>
  :root {
    --stage: #3b3b3d;
    --card-dark: #1c1c1d;
    --card-dark-mark: #2e2e30;
    --card-light: #ffffff;
    --ink: #1d1d1f;
    --red: #e8393d;
    --blue: #2b9fd8;
    --rule: #8a8a8a;
  }
  * { margin: 0; padding: 0; box-sizing: border-box; }
  html, body { width: 1200px; height: 901px; overflow: hidden; }
  body {
    background: var(--stage);
    display: flex;
    align-items: center;
    justify-content: center;
    gap: 40px;
    font-family: "Lato", sans-serif;
    color: var(--ink);
  }
  .card {
    width: 540px;
    height: 309px;
    border-radius: 18px;
    position: relative;
    overflow: hidden;
  }
  .card--front {
    background: var(--card-dark);
    display: flex;
    align-items: center;
    justify-content: center;
  }
  .front-wordmark {
    font-family: "Montserrat", sans-serif;
    font-weight: 800;
    font-size: 96px;
    letter-spacing: 2px;
    color: var(--card-dark-mark);
  }
  .card--back { background: var(--card-light); }
  .brand {
    position: absolute;
    left: 50px;
    top: 128px;
    display: flex;
    align-items: center;
    gap: 12px;
  }
  .brand__square { width: 22px; height: 22px; background: var(--red); }
  .brand__name {
    font-family: "Montserrat", sans-serif;
    font-weight: 800;
    font-size: 64px;
    line-height: 1;
    color: var(--ink);
  }
  .divider {
    position: absolute;
    left: 262px;
    top: 62px;
    width: 1px;
    height: 150px;
    background: var(--rule);
  }
  .contact {
    position: absolute;
    left: 282px;
    top: 58px;
  }
  .contact__name {
    font-family: "Montserrat", sans-serif;
    font-weight: 700;
    font-size: 22px;
    color: var(--red);
    line-height: 1.1;
  }
  .contact__title { font-size: 13px; margin-top: 2px; }
  .contact__address { font-size: 13px; line-height: 1.35; margin-top: 12px; }
  .contact__lines { list-style: none; margin-top: 12px; font-size: 13px; line-height: 1.5; }
  .contact__lines li { display: flex; align-items: center; gap: 8px; }
  .contact__lines svg { width: 13px; height: 13px; flex: none; }
  .partners {
    position: absolute;
    right: 34px;
    bottom: 32px;
    display: flex;
    align-items: baseline;
    gap: 28px;
    font-family: "Lato", sans-serif;
    font-weight: 700;
    font-size: 18px;
    line-height: 1;
  }
  .partner--durafilm { color: var(--blue); }
  .partner--velsun { color: var(--ink); }
</style>
</head>
<body>
  <section class="card card--front" aria-label="Card front">
    <span class="front-wordmark">RVL</span>
  </section>

  <section class="card card--back" aria-label="Card back">
    <div class="brand">
      <span class="brand__square"></span>
      <span class="brand__name">RVL</span>
    </div>

    <div class="divider"></div>

    <div class="contact">
      <p class="contact__name">Owen Marsh</p>
      <p class="contact__title">Sales Business Development</p>
      <p class="contact__address">2140 Harlow Drive<br>Oakridge, ON, K2P 4R8</p>
      <ul class="contact__lines">
        <li>
          <svg viewBox="0 0 16 16" aria-hidden="true"><path fill="var(--red)" d="M3.6 1.5l2.3 2.3-1.3 1.8c.9 2 2.5 3.6 4.5 4.5l1.8-1.3 2.3 2.3-1.6 2.4C6.8 13.3 2.7 9.2 1.2 4.4z"/></svg>
          (905) 555-0142
        </li>
        <li>
          <svg viewBox="0 0 16 16" aria-hidden="true"><rect x="1" y="3" width="14" height="10" fill="var(--red)"/><path d="M1 3l7 6 7-6" fill="none" stroke="#fff" stroke-width="1.3"/></svg>
          owen@rvlsuppliers.com
        </li>
      </ul>
    </div>

    <div class="partners">
      <span class="partner partner--durafilm">Durafilm Linings</span>
      <span class="partner partner--velsun">Velsun</span>
    </div>
  </section>
</body>
</html>
```